Start up in business consultancy needs a business card

We need the business card's layout (we have already the logo). Our business is concerned on consultancy services delivered to companies on the matter of sustainability. Business card should be enough essentials and professional style.

Side A with the following info:
logo + a space for the claim (still to identify) + website of the company

Side B with the following info:
Name of business card holder + title of the business card holder + address of the company + space for mobile number, phone number, fax number + e-mail of business card holder + graphic details around.

Target Market(s)

Business of any sector

Industry/Entity Type

Business Service

Contact Information for Business Card

Name of the company:
Pianoverde srl
Società Benefit

Address of the company:
Via Lucerna, 7
21047 - Saronno (VA)

Website:
www.pianoverde.it

Name of the BC' holder:
Luca Ferentino

Title:
Co-fondatore

Email:
luca@pianoverde.it

Mobile:
+39 348 915 2074
Phone:
+39 348 915 2074
Fax:
+39 348 915 2074

Font styles to use
Other font styles liked:
• new gothic

```html
<!DOCTYPE html>
<html lang="it">
<head>
<meta charset="utf-8">
<title>Pianoverde srl – Biglietto da visita</title>
<link rel="stylesheet" href="https://fonts.googleapis.com/css2?family=Open+Sans:wght@400;600&display=swap">
<style>
  :root {
    --brand-blue: #1670c9;
    --brand-blue-deep: #0c5aa8;
    --brand-blue-dark: #0b4f8f;
    --front-text: #e4effa;
    --ink: #222831;
    --paper: #ffffff;
    --paper-shade: #eef0f2;
    --backdrop: #d9dcdf;
  }
  * { box-sizing: border-box; margin: 0; padding: 0; }
  html, body {
    width: 1200px; height: 900px; overflow: hidden;
    background: var(--backdrop);
    font-family: "Open Sans", Arial, sans-serif;
  }
  .card-set {
    position: absolute; inset: 0;
    display: flex; align-items: center; justify-content: center; gap: 50px;
  }
  .card {
    position: relative;
    width: 540px; height: 350px;
    border-radius: 18px;
    overflow: hidden;
    box-shadow: 0 10px 28px rgba(0,0,0,0.22);
  }

  /* Side A */
  .card--front {
    background: linear-gradient(160deg, var(--brand-blue) 0%, var(--brand-blue-deep) 100%);
  }
  .card--front .mark-ring {
    position: absolute; left: 70px; top: -40px;
    width: 300px; height: 300px;
  }
  .card--front .front-name {
    position: absolute; right: 40px; top: 200px;
    font-size: 56px; font-weight: 400; letter-spacing: -0.5px; line-height: 1;
    color: var(--brand-blue-dark); opacity: 0.55;
  }
  .claim-space {
    position: absolute; left: 40px; right: 40px; top: 286px;
    height: 1px; background: var(--front-text); opacity: 0.35;
  }
  .front-website {
    position: absolute; right: 40px; bottom: 24px;
    font-size: 16px; font-weight: 400; color: var(--front-text);
  }

  /* Side B */
  .card--back {
    background: linear-gradient(135deg, var(--paper) 40%, var(--paper-shade) 100%);
    color: var(--ink);
  }
  .logo {
    position: absolute; right: 36px; top: 34px;
    display: flex; align-items: center; gap: 10px;
  }
  .logo-dot {
    width: 50px; height: 50px; border-radius: 50%;
    border: 3px solid var(--brand-blue-dark);
  }
  .logo-name {
    font-size: 28px; font-weight: 600; color: var(--brand-blue-dark);
  }
  .accent-bar {
    position: absolute; left: 290px; right: 0; top: 142px;
    height: 12px; background: var(--brand-blue-dark);
  }
  .holder {
    position: absolute; left: 56px; top: 122px;
  }
  .holder-name {
    font-size: 28px; font-weight: 400; color: var(--brand-blue-deep); line-height: 1.2;
  }
  .holder-title {
    font-size: 16px; margin-top: 8px;
  }
  .contacts {
    position: absolute; left: 56px; right: 36px; top: 232px;
    display: flex; justify-content: space-between;
    font-size: 17px; line-height: 1.3;
  }
  .contacts ul { list-style: none; }
</style>
</head>
<body>
  <main class="card-set">
    <section class="card card--front" aria-label="Lato A">
      <svg class="mark-ring" viewBox="0 0 300 300" aria-hidden="true">
        <circle cx="150" cy="150" r="135" fill="none" stroke="#0b4f8f" stroke-width="14" opacity="0.35"/>
      </svg>
      <p class="front-name">pianoverde</p>
      <div class="claim-space" aria-label="Spazio per il claim"></div>
      <p class="front-website">www.pianoverde.it</p>
    </section>

    <section class="card card--back" aria-label="Lato B">
      <div class="logo">
        <span class="logo-dot"></span>
        <span class="logo-name">pianoverde</span>
      </div>
      <div class="accent-bar"></div>
      <div class="holder">
        <h1 class="holder-name">Luca Ferentino</h1>
        <p class="holder-title">Co-fondatore</p>
      </div>
      <div class="contacts">
        <ul class="contacts-phone">
          <li>m. +39 348 915 2074</li>
          <li>p. +39 348 915 2074</li>
          <li>f. +39 348 915 2074</li>
        </ul>
        <ul class="contacts-web">
          <li>e. luca@pianoverde.it</li>
          <li>h. www.pianoverde.it</li>
          <li>l. Via Lucerna, 7</li>
          <li>&nbsp;&nbsp;&nbsp;21047 - Saronno (VA)</li>
        </ul>
      </div>
    </section>
  </main>
</body>
</html>
```